Modern Lawfirm Business Card Design

We're looking for a business card to incorporate the newly created logo we had made.

Ideally looking for a law firm business card demonstrating, modern, minimalist, strong/bold design.

I'm open to any design honestly, but nothing "flashy".

Target Market(s)

Immigration law, family immigration, humanitarian, general legal

Industry/Entity Type

Law Firm

Contact Information for Business Card

Please use dummy information, name, street address, city, state, phone number, email, website.

Font styles to use
Serif
Sans Serif

Requirements
Must have
• Please use dummy information, name, street address, city, state, phone number, email, website.

```html
<!DOCTYPE html>
<html lang="en">
<head>
<meta charset="utf-8">
<title>Calderwood Immigration Law – Business Card</title>
<link rel="stylesheet" href="https://fonts.googleapis.com/css2?family=Cinzel:wght@400;600&family=Open+Sans:wght@400;700&display=swap">
<style>
  :root {
    --navy: #1b3566;
    --navy-deep: #0f2450;
    --card-face: #eeeeec;
    --card-edge: #d8d8d6;
    --ink: #3c3f46;
    --stage: #cfccc8;
  }
  * { margin: 0; padding: 0; box-sizing: border-box; }
  html, body {
    width: 1200px;
    height: 969px;
    overflow: hidden;
    background: var(--stage);
  }
  .business-card {
    position: absolute;
    left: 100px;
    top: 198px;
    width: 1000px;
    height: 573px;
    background: linear-gradient(160deg, #f4f4f2 0%, var(--card-face) 55%, var(--card-edge) 100%);
    box-shadow: 0 18px 40px rgba(0,0,0,0.18);
    overflow: hidden;
  }
  .corner-band {
    position: absolute;
    inset: 0;
    width: 100%;
    height: 100%;
  }
  .firm-name {
    position: absolute;
    right: 57px;
    top: 72px;
    display: flex;
    align-items: center;
    gap: 14px;
  }
  .firm-name__square {
    width: 24px;
    height: 24px;
    background: var(--navy);
  }
  .firm-name__text {
    font-family: "Open Sans", sans-serif;
    font-weight: 700;
    font-size: 34px;
    color: var(--navy);
    line-height: 1;
  }
  .holder {
    position: absolute;
    right: 57px;
    top: 196px;
    text-align: right;
    font-family: "Cinzel", serif;
    color: var(--navy);
  }
  .holder__name {
    font-size: 37px;
    font-weight: 600;
    letter-spacing: 1px;
    line-height: 1.2;
  }
  .holder__title {
    font-size: 30px;
    font-weight: 400;
    color: var(--navy-deep);
    line-height: 1.3;
  }
  .contact {
    position: absolute;
    left: 52px;
    top: 335px;
    font-family: "Open Sans", sans-serif;
    font-size: 24px;
    color: var(--ink);
    line-height: 34px;
  }
  .contact__address { margin-bottom: 12px; }
  .contact__label {
    font-weight: 700;
    color: var(--navy);
  }
</style>
</head>
<body>
  <div class="business-card">
    <svg class="corner-band" viewBox="0 0 1000 573" preserveAspectRatio="none" aria-hidden="true">
      <polygon points="0,0 242,0 0,158" fill="var(--navy)"/>
      <polygon points="1000,409 1000,573 675,573" fill="var(--navy)"/>
    </svg>

    <div class="firm-name">
      <span class="firm-name__square"></span>
      <span class="firm-name__text">Calderwood Immigration Law</span>
    </div>

    <div class="holder">
      <div class="holder__name">MARTIN ELLERY</div>
      <div class="holder__title">President</div>
    </div>

    <div class="contact">
      <div class="contact__address">
        4120 Birchwood Court<br>
        Juneau, Alaska 99801
      </div>
      <div><span class="contact__label">Phone :</span> 555 218 4096</div>
      <div><span class="contact__label">Email :</span> martin@calderwoodlaw.com</div>
      <div><span class="contact__label">Web :</span> www.calderwoodlaw.com</div>
    </div>
  </div>
</body>
</html>
```